Top Real Estate teams new cards UPDATED

New Cards with MY (Im the tall guy in the middle) new pic on the front of card and my team pic on the back of card. Also my team name on the front of the card (marlow and partners) and brokerage name on the back (harborline real estate group) . Also the tag line "Ask about our 20 step plan" on the back of the card and "Welcome to the new way of Real Estate Sales" on the front of the card along with my phone number (951-482-3067) and email address (derek.marlow47@quillmail.net) my website (www.DerekMarlow.org) and my License number (BRE:07315294). I do like my team name colors of black and gold
Logo links are attached:
1. https://www.filevaultly.net/sh/815kqwz73hpadrx/AAG7MmK2PlR4ZqWsYnUuE_HQb?dl=0
2. https://www.filevaultly.net/sh/29c7vxm84tq015r/AACKDRLW46NeT2Gh8Vr4Jk7Yb?dl=0
Updates

Target Market(s)

Real Estate Customers

Industry/Entity Type

Real Estate

Contact Information for Business Card

Classy, yet east ro read and understand

Font styles to use
Sans Serif

Requirements
Must have
• Team and brokerage name, and both slogans.
• Black and gold color scheme.
Nice to have
• Bold writing
Should not have
• cluttered feeling

```html
<!DOCTYPE html>
<html lang="en">
<head>
<meta charset="utf-8">
<title>Marlow and Partners – Business Card</title>
<link rel="stylesheet" href="https://fonts.googleapis.com/css2?family=Cinzel:wght@400;600&family=Open+Sans:wght@400;600&display=swap">
<style>
  :root {
    --page: #e9e6e1;
    --card-black: #111111;
    --card-charcoal: #2a2a2a;
    --gold: #c9a92c;
    --gold-deep: #a88a1c;
    --white: #f2f2f2;
    --grey: #bdbdbd;
    --photo-warm-light: #8a7463;
    --photo-warm-mid: #5a4a40;
    --photo-cool-light: #6e6b68;
    --photo-cool-mid: #45423f;
  }
  * { margin: 0; padding: 0; box-sizing: border-box; }
  html, body { width: 771px; height: 1200px; overflow: hidden; background: var(--page); }
  .canvas { position: relative; width: 771px; height: 1200px; }

  .card {
    position: absolute; left: 45px; width: 680px; height: 388px;
    background: radial-gradient(ellipse at 35% 40%, var(--card-charcoal) 0%, var(--card-black) 75%);
    overflow: hidden; border-radius: 4px;
    box-shadow: 0 10px 24px rgba(0,0,0,.25);
  }
  .card--front { top: 150px; }
  .card--back { top: 662px; }

  /* Brand block */
  .brand { position: absolute; display: flex; align-items: center; gap: 14px; z-index: 1; }
  .brand__mark { width: 46px; height: 46px; border-radius: 50%; background: var(--gold); flex: none; }
  .brand__name {
    font-family: "Cinzel", serif; font-weight: 400; color: var(--white);
    text-transform: uppercase; line-height: 1.02; letter-spacing: .5px;
  }
  .tagline {
    position: absolute; font-family: "Cinzel", serif; font-weight: 400; color: var(--gold);
    text-transform: uppercase; letter-spacing: .6px; z-index: 1;
  }

  /* Front */
  .card--front .brand { left: 42px; top: 50px; }
  .card--front .brand__name { font-size: 26px; }
  .card--front .tagline { left: 42px; top: 120px; font-size: 12px; }
  .portrait {
    position: absolute; right: 0; top: 0; width: 320px; height: 250px;
    background: radial-gradient(ellipse at 35% 35%, var(--photo-warm-light) 0%, var(--photo-warm-mid) 45%, #2a2523 100%);
  }
  .identity { position: absolute; left: 42px; top: 160px; padding-left: 20px; }
  .identity::before {
    content: ""; position: absolute; left: 0; top: 4px; width: 8px; height: 52px; background: var(--gold);
  }
  .identity__name { font-family: "Cinzel", serif; font-weight: 400; font-size: 28px; color: var(--white); text-transform: uppercase; line-height: 1.1; }
  .identity__role { font-family: "Cinzel", serif; font-weight: 400; font-size: 16px; color: var(--gold); text-transform: uppercase; margin-top: 2px; }
  .contacts { position: absolute; left: 42px; top: 240px; list-style: none; }
  .contacts li {
    display: flex; align-items: center; gap: 12px; height: 32px;
    font-family: "Open Sans", sans-serif; font-size: 16px; color: var(--white);
  }
  .contacts svg { width: 16px; height: 16px; flex: none; }
  .contacts .contacts__license { font-size: 13px; color: var(--grey); padding-left: 28px; height: 26px; }

  /* Back */
  .team-photo {
    position: absolute; right: 0; top: 0; width: 370px; height: 300px;
    background: radial-gradient(ellipse at 50% 45%, var(--photo-cool-light) 0%, var(--photo-cool-mid) 50%, #262524 100%);
  }
  .gold-band {
    position: absolute; left: 0; right: 0; bottom: 0; height: 88px;
    background: linear-gradient(180deg, var(--gold) 0%, var(--gold-deep) 100%);
  }
  .card--back .brand { left: 42px; top: 130px; }
  .card--back .brand__mark { width: 58px; height: 58px; }
  .card--back .brand__name { font-size: 32px; }
  .card--back .tagline { left: 42px; top: 212px; font-size: 15px; }
  .brokerage {
    position: absolute; left: 42px; top: 250px;
    font-family: "Cinzel", serif; font-weight: 400; font-size: 14px; color: var(--white); text-transform: uppercase; letter-spacing: .5px;
  }
</style>
</head>
<body>
<main class="canvas">

  <section class="card card--front" aria-label="Card front">
    <div class="portrait" role="img" aria-label="Portrait photo of Derek Marlow in a dark suit"></div>
    <div class="brand">
      <span class="brand__mark"></span>
      <span class="brand__name">Marlow and<br>Partners</span>
    </div>
    <p class="tagline">Welcome to the new way of Real Estate Sales</p>
    <div class="identity">
      <h1 class="identity__name">Derek Marlow</h1>
      <p class="identity__role">Job Title</p>
    </div>
    <ul class="contacts">
      <li>
        <svg viewBox="0 0 16 16" aria-hidden="true"><path fill="#c9a92c" d="M3 2h3l1 3-2 1c1 2 2 3 4 4l1-2 3 1v3c0 1-1 2-2 2C6 14 2 10 2 4c0-1 0-2 1-2z"/></svg>
        951-482-3067
      </li>
      <li>
        <svg viewBox="0 0 16 16" aria-hidden="true"><rect x="1" y="3" width="14" height="10" fill="#c9a92c"/><path d="M1 3l7 6 7-6" fill="none" stroke="#111" stroke-width="1.4"/></svg>
        derek.marlow47@quillmail.net
      </li>
      <li>
        <svg viewBox="0 0 16 16" aria-hidden="true"><circle cx="8" cy="8" r="6.5" fill="none" stroke="#c9a92c" stroke-width="1.5"/><path d="M1.5 8h13M8 1.5c-3 3.5-3 9.5 0 13M8 1.5c3 3.5 3 9.5 0 13" fill="none" stroke="#c9a92c" stroke-width="1.2"/></svg>
        www.DerekMarlow.org
      </li>
      <li class="contacts__license">BRE:07315294</li>
    </ul>
  </section>

  <section class="card card--back" aria-label="Card back">
    <div class="team-photo" role="img" aria-label="Team photo of three agents in black standing together"></div>
    <div class="gold-band"></div>
    <div class="brand">
      <span class="brand__mark"></span>
      <span class="brand__name">Marlow and<br>Partners</span>
    </div>
    <p class="tagline">Ask about our 20 step plan</p>
    <p class="brokerage">Harborline Real Estate Group</p>
  </section>

</main>
</body>
</html>
```